Up to the Challenge? Canadian based consulting company needs a two sided business card design

A Canadian based security risk management consulting company needs a two-sided business card design. What we do is provide advice and guidance related to emergency, security and business continuity management for small, medium and large companies to help ensure the protection of their people, assets, information, services, operations and reputation.

The final design should be simple, only one or two colours, eye catching, professional and one that makes people look at three or more times just because it looks so darn good.

I have include examples of business cards I like.

Target Market(s)

Small, medium and large companies.

Industry/Entity Type

Security

Contact Information for Business Card

Business Card Size: Standard size of 3.5" (89mm) x 2.0" (51mm) - (see full specifications and guides on PRINTA's website if required)
Card Stock: Looking to use PRINTA's Velda 32pt stock textured paper - seam colour either chili red or black
Business Name: The Harrowfield Group
Website: www.theharrowfieldgroup.example
Telephone: (555)214-0397
Name: Dana Forsythe
Position: Principle
e-mail: Dana.Forsythe@theharrowfieldgroup.example

Font styles to use
Serif

Colors
ec1f27
000000
9d9d9d
aaaaaa
606060

Requirements
Must have
• - "The Harrowfield Group" logo (see uploaded files). I have included grey scale and colour versions.
• - Business card details (as above)
Nice to have
• - One side black or grey scale.
• - Other side would likely be white.
• - Everyone likes the silver logo on the black background.
• - Small element of colour i.e. red but I'm leaning more to greyscale.
Should not have
• - A lot of colour. Keep it simple.

```html
<!DOCTYPE html>
<html lang="en">
<head>
<meta charset="utf-8">
<title>The Harrowfield Group — Business Card</title>
<link href="https://fonts.googleapis.com/css2?family=Montserrat:wght@400;600;700&display=swap" rel="stylesheet">
<style>
  :root {
    --backdrop: #2e2e2e;
    --card-white: #ffffff;
    --card-black: #050505;
    --brand-red: #ec1f27;
    --ink-dark: #606060;
    --ink-mid: #9d9d9d;
    --silver: #aaaaaa;
  }
  * { margin: 0; padding: 0; box-sizing: border-box; }
  html, body {
    width: 1200px;
    height: 701px;
    overflow: hidden;
    background: var(--backdrop);
    font-family: "Montserrat", sans-serif;
  }
  .canvas {
    position: relative;
    width: 1200px;
    height: 701px;
    display: flex;
    align-items: center;
    justify-content: center;
    gap: 60px;
  }
  .card {
    position: relative;
    width: 500px;
    height: 286px;
    box-shadow: 0 10px 30px rgba(0,0,0,.45);
  }
  .card--back {
    background: var(--card-black);
    display: flex;
    align-items: center;
    justify-content: center;
  }
  .card--front { background: var(--card-white); }

  .brand-mark {
    display: flex;
    align-items: center;
    gap: 10px;
    font-weight: 700;
    letter-spacing: 0.06em;
    text-transform: uppercase;
  }
  .brand-mark__square { width: 14px; height: 14px; flex: none; }
  .card--back .brand-mark { color: var(--silver); font-size: 15px; }
  .card--back .brand-mark__square { background: var(--silver); }

  .card--front .brand-mark {
    position: absolute;
    right: 34px;
    top: 92px;
    color: var(--brand-red);
    font-size: 14px;
  }
  .card--front .brand-mark__square { background: var(--brand-red); }

  .contact {
    position: absolute;
    left: 38px;
    top: 118px;
  }
  .contact__name {
    font-size: 15px;
    font-weight: 700;
    color: var(--ink-dark);
    letter-spacing: 0.03em;
    text-transform: uppercase;
  }
  .contact__role {
    font-size: 11px;
    font-weight: 700;
    color: var(--brand-red);
    margin-top: 1px;
  }
  .contact__details {
    list-style: none;
    margin-top: 8px;
    padding-left: 10px;
    border-left: 2px solid var(--brand-red);
    font-size: 10.5px;
    line-height: 1.5;
    color: var(--ink-dark);
  }
</style>
</head>
<body>
  <main class="canvas">
    <section class="card card--back" aria-label="Card back">
      <div class="brand-mark">
        <span class="brand-mark__square"></span>
        <span>The Harrowfield Group</span>
      </div>
    </section>

    <section class="card card--front" aria-label="Card front">
      <div class="contact">
        <p class="contact__name">Dana Forsythe</p>
        <p class="contact__role">Principle</p>
        <ul class="contact__details">
          <li>(555)214-0397</li>
          <li>Dana.Forsythe@theharrowfieldgroup.example</li>
          <li>ca.profilelink.example/in/danaforsythe</li>
          <li>www.theharrowfieldgroup.example</li>
        </ul>
      </div>
      <div class="brand-mark">
        <span class="brand-mark__square"></span>
        <span>The Harrowfield Group</span>
      </div>
    </section>
  </main>
</body>
</html>
```